Reef Glow

sunglasses, sihoullette of body, maybe wearing a bikini or sunglasses. I am offering spray tanning, body wraps, tanning beds, stand up, body art, airbrush makeup.

Target Market(s)

I would say my target is all ages, But tanning is a seasonal business and more beauty and aging concept. and around prom time I get my most profitable business. so 18 to 21 through march and april. then 25 to 55 through april to june.

Industry/Entity Type

Makeup

Contact Information for Business Card

Phone number: 701-382-5147 Owner: Jan Mortby (Lisowski)

Colors

Designer to choose colors to be used in the design.

Requirements
Nice to have
• Sunglasses, silouttes of body wearing sunglasses or bikini, or picture of spray gun.

```html
<!DOCTYPE html>
<html lang="en">
<head>
<meta charset="utf-8">
<title>Reef Glow — Business Card</title>
<link rel="stylesheet" href="https://fonts.googleapis.com/css2?family=Questrial&family=Oswald:wght@600&display=swap">
<style>
  :root {
    --stage: #e9e7e4;
    --card-white: #ffffff;
    --card-white-shade: #e6e6e6;
    --card-black: #0c0c0c;
    --pattern-tone: #262626;
    --orange: #f28c1a;
    --amber: #f7b21b;
    --yellow: #ffe21a;
    --text-light: #f4f4f4;
    --ink: #111111;
  }
  * { margin: 0; padding: 0; box-sizing: border-box; }
  html, body {
    width: 1200px; height: 800px; overflow: hidden;
    background: var(--stage);
  }
  .business-card {
    position: absolute; left: 150px; top: 143px;
    width: 900px; height: 514px;
    background: var(--card-black);
    box-shadow: 0 18px 40px rgba(0,0,0,0.25);
    overflow: hidden;
    font-family: "Questrial", "Century Gothic", sans-serif;
  }
  .card-top {
    position: absolute; left: 0; top: 0; width: 100%; height: 232px;
    background: linear-gradient(180deg, var(--card-white) 0%, var(--card-white) 55%, var(--card-white-shade) 100%);
  }
  .brand {
    position: absolute; left: 96px; top: 62px;
    display: flex; align-items: center; gap: 22px;
  }
  .brand-dot {
    width: 54px; height: 54px; border-radius: 50%;
    background: var(--orange);
  }
  .brand-name {
    font-size: 104px; line-height: 1; color: var(--orange);
    letter-spacing: 1px;
  }
  .services-band {
    position: absolute; left: 0; top: 232px; width: 100%; height: 30px;
    background: var(--orange);
  }
  .services-list {
    position: absolute; right: 0; top: 4px; height: 22px;
    padding: 0 14px 0 40px;
    background: var(--yellow);
    clip-path: polygon(14px 0, 100% 0, 100% 100%, 0 100%);
    font-family: "Oswald", "Arial Narrow", sans-serif;
    font-weight: 600; font-size: 16px; line-height: 22px;
    letter-spacing: 1.2px; color: var(--ink); text-transform: uppercase;
  }
  .card-pattern {
    position: absolute; left: 0; top: 262px; width: 100%; height: 252px;
    background: radial-gradient(ellipse at 70% 40%, var(--pattern-tone) 0%, var(--card-black) 75%);
  }
  .contact {
    position: absolute; left: 118px; top: 300px; color: var(--text-light);
  }
  .owner-name { font-size: 28px; color: var(--amber); letter-spacing: 0.5px; }
  .owner-role { font-size: 20px; margin-top: 10px; }
  .phone-list { list-style: none; margin-top: 18px; }
  .phone {
    display: flex; align-items: center; gap: 12px;
    font-size: 34px; line-height: 1.15; letter-spacing: 1px;
  }
  .phone svg { width: 26px; height: 30px; flex: none; }
</style>
</head>
<body>
  <article class="business-card">
    <section class="card-top">
      <div class="brand">
        <span class="brand-dot"></span>
        <span class="brand-name">Reef Glow</span>
      </div>
    </section>

    <div class="services-band">
      <p class="services-list">Spray tanning, body wraps, tanning beds, stand up, body art, airbrush makeup</p>
    </div>

    <div class="card-pattern" role="img" aria-label="Dark grey damask flourish pattern on black"></div>

    <section class="contact">
      <h1 class="owner-name">Jan Mortby (Lisowski)</h1>
      <p class="owner-role">Owner</p>
      <ul class="phone-list">
        <li class="phone">
          <svg viewBox="0 0 26 30" aria-hidden="true">
            <rect x="6" y="2" width="14" height="26" rx="2" fill="var(--amber)"/>
            <rect x="8.5" y="5" width="9" height="8" fill="var(--card-black)"/>
            <rect x="8.5" y="16" width="2.5" height="2" fill="var(--card-black)"/>
            <rect x="12" y="16" width="2.5" height="2" fill="var(--card-black)"/>
            <rect x="15" y="16" width="2.5" height="2" fill="var(--card-black)"/>
            <rect x="8.5" y="20" width="2.5" height="2" fill="var(--card-black)"/>
            <rect x="12" y="20" width="2.5" height="2" fill="var(--card-black)"/>
            <rect x="15" y="20" width="2.5" height="2" fill="var(--card-black)"/>
          </svg>
          <span>(701) 555-0148</span>
        </li>
        <li class="phone">
          <svg viewBox="0 0 26 30" aria-hidden="true">
            <path d="M5 8c0-2 2-4 4-4l3 5-2 3c1 3 3 5 6 6l3-2 5 3c0 2-2 4-4 4C11 23 5 16 5 8z" fill="var(--amber)"/>
          </svg>
          <span>(701) 382-5147</span>
        </li>
      </ul>
    </section>
  </article>
</body>
</html>
```